Ad to be used on social media.

____________________________________________________________________________

Bored at Home?

Study to become a
Virtual Mortgage Originator today...

Complete 20 Hour Online Course & State Exam
in 30 days or less

Earn $3,000 to $5,000 on average per loan
No Work Hours, Goals or Quotas
Full Time or Part Time Opportunities

Email us at employment@brightpathlending.com

Crestmoor Financial Services, Inc.
4172 Wendover Lane
Ellicott City, MD 21043
(800) 647-2091
www.brightpathlending.com
NMLS #318760

```html
<!DOCTYPE html>
<html lang="en">
<head>
<meta charset="utf-8">
<title>Bored at Home? Study to become a Virtual Mortgage Originator</title>
<link rel="stylesheet" href="https://fonts.googleapis.com/css2?family=Bebas+Neue&family=Lexend:wght@300;400;500;600;700&family=Montserrat:wght@500;700;800&display=swap">
<style>
  :root {
    --ocean: #0b5d89;
    --lime: #a3cf3a;
    --lime-strong: #8cc43a;
    --fold: #356716;
    --white: #ffffff;
    --ink-blue: #134f7e;
    --footer-bar: #dfe4ea;
  }
  * { box-sizing: border-box; margin: 0; padding: 0; }
  html, body { width: 960px; height: 1200px; overflow: hidden; background: var(--white); }
  .ad {
    position: relative;
    width: 960px;
    height: 1200px;
    overflow: hidden;
    font-family: "Lexend", sans-serif;
  }
  .hero-photo {
    position: absolute;
    left: 0; top: 0;
    width: 960px; height: 526px;
    background:
      radial-gradient(ellipse 340px 300px at 280px 270px, #cfd8a8 0%, rgba(207,216,168,0) 70%),
      linear-gradient(180deg, #c9d1db 0%, #aeb9c6 60%, #eef0f2 92%, #f6f6f6 100%);
  }
  .headline {
    position: absolute;
    left: 554px; top: 146px;
    font-family: "Bebas Neue", sans-serif;
    font-weight: 400;
    font-size: 130px;
    line-height: 114px;
    color: var(--white);
    letter-spacing: -1px;
  }
  .offer {
    position: absolute;
    left: 0; top: 526px;
    width: 960px; height: 494px;
    background: var(--ocean);
  }
  .offer-art { position: absolute; left: 0; top: 0; width: 960px; height: 1200px; }
  .perks {
    position: absolute;
    left: 494px; top: 930px;
    list-style: none;
    color: var(--white);
    font-size: 23px;
    line-height: 41px;
    white-space: nowrap;
  }
  .perks li::before {
    content: "";
    display: inline-block;
    width: 9px; height: 9px;
    border-radius: 50%;
    background: var(--white);
    margin-right: 14px;
    vertical-align: middle;
    position: relative; top: -2px;
  }
  .footer-bar {
    position: absolute;
    left: 0; top: 1020px;
    width: 960px; height: 49px;
    background: linear-gradient(90deg, var(--white) 0%, var(--white) 35%, var(--footer-bar) 100%);
  }
  .footer-text {
    position: absolute;
    line-height: 1;
    white-space: nowrap;
    color: var(--ink-blue);
  }
  .email { left: 417px; top: 1035px; font-size: 18px; font-weight: 400; }
  .email strong { font-size: 22px; font-weight: 500; }
  .company { left: 417px; top: 1084px; font-size: 24px; font-weight: 500; }
  .address { left: 417px; top: 1121px; font-size: 19px; font-weight: 300; }
  .phone { left: 416px; top: 1153px; font-size: 31px; font-weight: 300; }
  .license { left: 681px; top: 1162px; font-size: 20px; font-weight: 300; }
  .website { left: 60px; top: 1166px; font-size: 18px; font-weight: 500; }
  .brand {
    position: absolute;
    left: 86px; top: 1080px;
    display: flex; align-items: center; gap: 10px;
    font-size: 24px; font-weight: 600; line-height: 1;
    color: var(--ocean);
  }
  .brand-dot { width: 24px; height: 24px; border-radius: 50%; background: var(--lime-strong); }
</style>
</head>
<body>
<main class="ad">
  <div class="hero-photo" role="img" aria-label="Photo of a bored girl in a green shirt and face mask resting her head on her hand at a table"></div>
  <h1 class="headline">BORED<br>AT HOME?</h1>

  <section class="offer"></section>

  <svg class="offer-art" viewBox="0 0 960 1200">
    <text x="56" y="631" fill="var(--lime)" font-family="Lexend, sans-serif" font-weight="300" font-size="116">Study</text>
    <text x="411" y="631" fill="var(--lime)" font-family="Lexend, sans-serif" font-weight="300" font-size="36">to become a</text>
    <text x="56" y="700" fill="var(--white)" font-family="Montserrat, sans-serif" font-weight="700" font-size="48" textLength="698" lengthAdjust="spacingAndGlyphs">Virtual Mortgage Originator</text>
    <text x="766" y="700" fill="var(--lime)" font-family="Lexend, sans-serif" font-weight="300" font-size="37" textLength="141" lengthAdjust="spacingAndGlyphs">today...</text>

    <polygon points="529,908 571,846 556,848" fill="var(--fold)"/>
    <polygon points="0,800 558,733 571,846 0,916" fill="var(--lime)"/>
    <polygon points="565,788 960,740 960,858 529,908" fill="var(--lime-strong)"/>

    <g transform="translate(34 847) rotate(-6.8)" fill="var(--white)">
      <text x="0" y="0" font-family="Montserrat, sans-serif" font-weight="700" font-size="22" textLength="513" lengthAdjust="spacingAndGlyphs">Complete <tspan font-family="Lexend, sans-serif" font-weight="400" font-size="36">20 Hour</tspan> <tspan font-family="Lexend, sans-serif" font-weight="400" font-size="26">Online Course</tspan></text>
      <text x="4" y="36" font-family="Montserrat, sans-serif" font-weight="700" font-size="22" textLength="420" lengthAdjust="spacingAndGlyphs">&amp; State Exam in 30 days or less</text>
    </g>
    <g transform="translate(601 843) rotate(-7.2)" fill="var(--white)" font-family="Lexend, sans-serif" font-weight="300">
      <text x="0" y="0" font-size="27" textLength="340" lengthAdjust="spacingAndGlyphs">Earn $<tspan font-family="Montserrat, sans-serif" font-weight="800" font-size="30">3,000</tspan> to $<tspan font-family="Montserrat, sans-serif" font-weight="800" font-size="30">5,000</tspan></text>
      <text x="4" y="34" font-size="27" textLength="272" lengthAdjust="spacingAndGlyphs">on average per loan</text>
    </g>
  </svg>

  <ul class="perks">
    <li>No Work Hours, Goals or Quotas</li>
    <li>Full Time or Part Time Opportunities</li>
  </ul>

  <div class="footer-bar"></div>
  <p class="footer-text email">Email us at <strong>employment@brightpathlending.com</strong></p>
  <div class="brand"><span class="brand-dot"></span><span>Crestmoor</span></div>
  <p class="footer-text website">www.brightpathlending.com</p>
  <p class="footer-text company">Crestmoor Financial Services, Inc.</p>
  <p class="footer-text address">4172 Wendover Lane, Ellicott City, MD 21043</p>
  <p class="footer-text phone">(800) 647-2091</p>
  <p class="footer-text license">NMLS #318760</p>
</main>
</body>
</html>
```